Business card - Brio Margin - size 85 mm * 55 mm

We need new business cards. Design must fit with our vision of the firm. You find in the attached file our logo and a short description of our firm (mission, vision, value, business and so on).

Target Market(s)

Consulting firm in performance improvement

Industry/Entity Type

Management Consulting

Contact Information for Business Card

SIZE
85 mm * 55 mm
INFORMATIONS
name surname
role position
telephone number
email address

Requirements
Must have
• the brand must APPEAR for the rest Would we like to have something sleek, inspired to a "just right" approach
Should not have
• Please avoid the black color as background

```html
<!DOCTYPE html>
<html lang="en">
<head>
<meta charset="utf-8">
<title>Brio Margin – Business Card</title>
<link rel="stylesheet" href="https://fonts.googleapis.com/css2?family=Barlow+Semi+Condensed:wght@400;500&display=swap">
<style>
  :root {
    --page-bg: #e9e4de;
    --card-clear: #d9d6cf;
    --card-edge: #f4f2ee;
    --green-light: #6fb62c;
    --green-mid: #4f9a1e;
    --green-deep: #3a7a14;
    --ink-silver: #e8e0d6;
    --rule: rgba(232, 224, 214, 0.55);
  }
  * { box-sizing: border-box; margin: 0; padding: 0; }
  html, body { width: 1200px; height: 751px; overflow: hidden; }
  body {
    background: var(--page-bg);
    font-family: "Barlow Semi Condensed", "Arial Narrow", sans-serif;
    position: relative;
  }
  .card {
    position: absolute;
    top: 214px;
    width: 500px;
    height: 324px;
    background: var(--card-clear);
    border: 1px solid var(--card-edge);
    overflow: hidden;
  }
  .card--front { left: 60px; }
  .card--back { left: 640px; }

  .brush-field {
    position: absolute;
    top: 0;
    bottom: 0;
  }
  .card--front .brush-field {
    right: 0;
    width: 64%;
    background: linear-gradient(160deg, var(--green-light) 0%, var(--green-mid) 55%, var(--green-deep) 100%);
  }
  .card--back .brush-field {
    left: 0;
    width: 56%;
    background: linear-gradient(200deg, var(--green-light) 0%, var(--green-mid) 55%, var(--green-deep) 100%);
  }

  .contact {
    position: absolute;
    right: 34px;
    top: 160px;
    text-align: right;
    color: var(--ink-silver);
  }
  .contact__name {
    font-size: 24px;
    font-weight: 400;
    letter-spacing: 0.5px;
    line-height: 1;
  }
  .contact__role {
    font-size: 14px;
    margin-top: 6px;
    letter-spacing: 0.4px;
  }
  .contact__rule {
    width: 136px;
    height: 1px;
    background: var(--rule);
    margin: 10px 0 12px auto;
  }
  .contact__line {
    font-size: 14px;
    letter-spacing: 0.4px;
    line-height: 23px;
  }

  .brand {
    position: absolute;
    left: 38px;
    top: 170px;
    width: 210px;
    text-align: center;
    color: var(--ink-silver);
  }
  .brand__dot {
    display: block;
    width: 76px;
    height: 76px;
    margin: 0 auto 20px;
    border: 3px solid var(--ink-silver);
    border-radius: 50%;
  }
  .brand__name {
    font-size: 17px;
    font-weight: 500;
    letter-spacing: 5px;
    white-space: nowrap;
  }
</style>
</head>
<body>
  <section class="card card--front">
    <div class="brush-field" role="img" aria-label="Green brush-stroke brand pattern"></div>
    <div class="contact">
      <p class="contact__name">ALAN REYES</p>
      <p class="contact__role">CEO/FOUNDER</p>
      <div class="contact__rule"></div>
      <p class="contact__line">555 014 2290</p>
      <p class="contact__line">ALAN@BRIOMARGIN.COM</p>
      <p class="contact__line">WWW.BRIOMARGIN.COM</p>
    </div>
  </section>

  <section class="card card--back">
    <div class="brush-field" role="img" aria-label="Green brush-stroke brand pattern"></div>
    <div class="brand">
      <span class="brand__dot"></span>
      <p class="brand__name">BRIO MARGIN</p>
    </div>
  </section>
</body>
</html>
```